Packaging design for Prenatal, Fish Oil, and Joint Pain product

We are looking for package design (label and outer box) for following products:
1) Moreval
- Product name: Moreval
- Benefit: Prenatal
- Feature DHA + Folic Acid
- What we need from you? We need box concept
- Box dimension 55mm Height x 145mm length x 100mm width
2) Omega 3 Alaskan Salmon
- Product name: Omega 3 Alaskan Salmon
- Benefit: Cognitive , cardiovascular Health, Joint Health, High cholesterol
- Feature: Alaskan Salmon
- What we need from you? We need label concept
- Label dimension: 60mm Height x 180mm Length
2) Quorba
- Product name: Quorba
- Benefit: Joint Health
- Feature: Glucosamin, Chondroitin, MSM
Designer can use generic text on other vitamin products for formula, usage instruction etc.
We have logo. The logo must be integrated in the packaging design. (please see attachment)

```html
<!DOCTYPE html>
<html lang="en">
<head>
<meta charset="utf-8">
<title>Moreval Prenatal – Box Dieline</title>
<link rel="stylesheet" href="https://fonts.googleapis.com/css2?family=Jost:wght@400;500&display=swap">
<style>
  :root {
    --page: #ffffff;
    --cut-line: #d9d9d9;
    --panel: #ffffff;
    --strip-grey: #d5d1cb;
    --brand-block: #231f20;
    --band-light: #e9dbb0;
    --band-gold: #edd28f;
    --ink: #231f20;
    --reverse: #ffffff;
  }
  html, body {
    margin: 0;
    width: 1200px;
    height: 900px;
    overflow: hidden;
    background: var(--page);
  }
  .dieline { display: block; width: 1200px; height: 900px; }
  .sheet-frame { fill: none; stroke: #ececec; stroke-width: 1; }
  .panel { fill: var(--panel); stroke: var(--cut-line); stroke-width: 1; }
  .flap-gold { fill: var(--band-gold); stroke: var(--cut-line); stroke-width: 1; }
  .fold { stroke: var(--cut-line); stroke-width: 1; }
  .band-feature { fill: var(--band-light); }
  .band-name { fill: var(--band-gold); }
  .label-strip { fill: var(--strip-grey); }
  .brand-block { fill: var(--brand-block); }
  .benefit {
    font-family: "Jost", sans-serif;
    font-size: 27px;
    letter-spacing: 1px;
    fill: var(--ink);
  }
  .feature {
    font-family: "Jost", sans-serif;
    font-weight: 500;
    font-size: 11px;
    fill: var(--ink);
  }
  .product-name {
    font-family: "Jost", sans-serif;
    font-weight: 500;
    font-size: 30px;
    fill: var(--reverse);
  }
  .brand-name {
    font-family: "Jost", sans-serif;
    font-weight: 500;
    font-size: 20px;
    fill: var(--reverse);
  }
</style>
</head>
<body>
<svg class="dieline" viewBox="0 0 1200 900" xmlns="http://www.w3.org/2000/svg">
  <defs>
    <clipPath id="body-clip">
      <path d="M219,275 H990 L1015,285 V625 L990,635 H219 Z"/>
    </clipPath>
  </defs>

  <rect class="sheet-frame" x="3" y="40" width="1194" height="830"/>

  <!-- top closure -->
  <path class="panel" d="M219,138 L240,113 H447 L468,138 V275 H219 Z"/>
  <line class="fold" x1="219" y1="138" x2="468" y2="138"/>
  <path class="panel" d="M468,275 L468,262 Q478,255 480,240 L485,150 Q487,139 497,138 L605,138 L605,275 Z"/>
  <path class="panel" d="M853,138 L960,138 Q970,139 972,150 L977,240 Q979,255 990,262 L990,275 L853,275 Z"/>

  <!-- bottom closure -->
  <path class="flap-gold" d="M468,635 L605,635 L605,650 Q597,655 596,670 L592,760 Q590,771 580,772 L468,772 Z"/>
  <path class="flap-gold" d="M853,635 L990,635 L990,772 L878,772 Q868,771 866,760 L862,670 Q861,655 853,650 Z"/>
  <path class="flap-gold" d="M605,635 H853 V772 L828,797 H630 L605,772 Z"/>
  <line class="fold" x1="605" y1="772" x2="853" y2="772"/>

  <!-- box body -->
  <g clip-path="url(#body-clip)">
    <rect class="panel" x="219" y="275" width="800" height="360"/>
    <rect class="band-feature" x="219" y="517" width="800" height="21"/>
    <rect class="band-name" x="219" y="538" width="800" height="97"/>
  </g>
  <path d="M219,275 H990 L1015,285 V625 L990,635 H219 Z" fill="none" stroke="var(--cut-line)"/>
  <line class="fold" x1="468" y1="275" x2="468" y2="635"/>
  <line class="fold" x1="605" y1="275" x2="605" y2="635"/>
  <line class="fold" x1="853" y1="275" x2="853" y2="635"/>
  <line class="fold" x1="990" y1="275" x2="990" y2="635"/>

  <!-- front panel -->
  <g class="front-panel">
    <rect class="label-strip" x="317" y="113" width="54" height="385"/>
    <rect class="brand-block" x="317" y="445" width="54" height="53"/>
    <text class="brand-name" x="344" y="478" text-anchor="middle">evi</text>
    <text class="benefit" transform="translate(353,441) rotate(-90)">PRENATAL</text>
    <text class="feature" x="343" y="531" text-anchor="middle">Feature DHA + Folic Acid</text>
    <text class="product-name" x="344" y="597" text-anchor="middle">Moreval</text>
  </g>

  <!-- back panel -->
  <g class="back-panel">
    <rect class="label-strip" x="701" y="275" width="54" height="223"/>
    <rect class="brand-block" x="701" y="445" width="54" height="53"/>
    <text class="brand-name" x="728" y="478" text-anchor="middle">evi</text>
    <text class="benefit" transform="translate(737,441) rotate(-90)">PRENATAL</text>
    <text class="feature" x="727" y="531" text-anchor="middle">Feature DHA + Folic Acid</text>
    <text class="product-name" x="729" y="597" text-anchor="middle">Moreval</text>
  </g>
</svg>
</body>
</html>
```